Design concept for BrightKestrel.com Support Page

We are about to launch a new support page for our www.brightkestrel.com service for photographers and visual artists. The service provides media management, cloud storage, promotional and secure distribution to our members.

The support page will include FAQs and video tutorials.

In particular we're looking for a header for this page that suggests the user is in the support area of our service - so perhaps an illustration that suggests support could look nice (perhaps repair man or doctor iconography). Something to give this area of our site a different look and something that looks both cool and friendly.

Currently the page looks distinctly sparse and undesigned (see attached screenshot) - something that could be remedied, we feel, by some subtle design enhancements that we can implement using CSS.

```html
<!DOCTYPE html>
<html lang="en">
<head>
<meta charset="utf-8">
<title>BrightKestrel Support Center</title>
<link href="https://fonts.googleapis.com/css2?family=Nunito+Sans:ital,wght@0,400;0,600;0,700;1,400&display=swap" rel="stylesheet">
<style>
  :root {
    --ink: #1a1a1a;
    --black: #0c0c0c;
    --red: #ee2a24;
    --rule: #e3e3e3;
    --white: #ffffff;
    --font: "Nunito Sans", Arial, sans-serif;
  }
  * { box-sizing: border-box; margin: 0; padding: 0; }
  html, body { width: 1200px; height: 1200px; overflow: hidden; background: var(--white); }
  body { position: relative; font-family: var(--font); color: var(--ink); letter-spacing: 0.04em; }
  .abs { position: absolute; }

  .topbar { left: 0; top: 0; width: 1200px; height: 52px; background: var(--black); }
  .brand { left: 138px; top: 9px; display: flex; align-items: center; gap: 8px; color: var(--white); font-weight: 700; font-size: 27px; letter-spacing: 0; }
  .brand-mark { width: 28px; height: 28px; border: 3px solid var(--white); border-radius: 4px; }

  .photo-strip { left: 0; top: 52px; width: 1200px; height: 200px; display: flex; }
  .photo-strip div { height: 100%; }
  .ph-arch { width: 315px; background: linear-gradient(100deg, #d99a2b 0%, #e8b14a 30%, #2d5c93 55%, #b98532 85%); }
  .ph-festival { width: 136px; background: linear-gradient(180deg, #d9488a, #c3353d 60%, #e3a33a); }
  .ph-canal { width: 136px; background: linear-gradient(180deg, #6d7252, #3d4a33 55%, #c9a12c 90%); }
  .ph-study { width: 323px; background: linear-gradient(90deg, #c8c8c8, #7a7a7a 50%, #3e3e3e); }
  .ph-gathering { width: 290px; background: linear-gradient(100deg, #2e3f55, #7a5a3c 55%, #b0703e); }

  .intro { left: 0; width: 1200px; text-align: center; }
  .intro-title { top: 296px; font-size: 24px; font-weight: 400; }
  .intro-sub { top: 336px; font-size: 15px; }
  .rule { height: 1px; background: var(--rule); }

  .feature { width: 220px; }
  .feature-icon { width: 100px; height: 100px; border: 2px solid var(--red); border-radius: 50%; display: flex; align-items: center; justify-content: center; color: var(--red); }
  .feature-title { font-size: 15.5px; font-weight: 600; margin-top: 11px; letter-spacing: 0.06em; }
  .feature-text { font-size: 13px; line-height: 20.8px; margin-top: 9px; }
  .feature-btn { display: block; width: 162px; height: 28px; margin-top: 8px; margin-left: -1px; background: var(--red); color: var(--white); font-size: 13px; line-height: 28px; padding-left: 14px; border-radius: 2px; }

  .notch { left: 576px; top: 760px; width: 0; height: 0; border-left: 10px solid transparent; border-right: 10px solid transparent; border-top: 10px solid var(--rule); }
  .notch::after { content: ""; position: absolute; left: -9px; top: -11px; border-left: 9px solid transparent; border-right: 9px solid transparent; border-top: 9px solid var(--white); }

  .section-title { color: var(--red); font-size: 20.5px; font-weight: 400; }
  .view-all { left: 965px; top: 824px; font-size: 11.5px; font-style: italic; letter-spacing: 0.02em; border-bottom: 1px solid var(--ink); line-height: 13px; }
  .view-all::after { content: ""; position: absolute; right: -10px; top: 3px; border-left: 5px solid var(--ink); border-top: 3.5px solid transparent; border-bottom: 3.5px solid transparent; }

  .video { text-align: center; }
  .video-thumb { position: relative; height: 142px; display: flex; align-items: center; justify-content: center; }
  .play { width: 72px; height: 72px; border: 2.5px solid rgba(255,255,255,0.85); border-radius: 50%; display: flex; align-items: center; justify-content: center; background: rgba(255,255,255,0.12); }
  .video-caption { color: var(--red); font-size: 14.5px; line-height: 20.5px; margin-top: 16px; }

  .search-box { left: 810px; top: 1196px; width: 222px; height: 20px; border: 1px solid #cfcfcf; }
  .search-btn { left: 994px; top: 1196px; width: 38px; height: 20px; background: var(--red); }

  .live-help { left: 1167px; top: 481px; width: 33px; height: 128px; background: #1c1c1c; border-radius: 3px 0 0 3px; color: var(--white); }
  .live-help span { position: absolute; left: 7px; top: 22px; writing-mode: vertical-rl; font-size: 14px; font-weight: 600; letter-spacing: 0.02em; }
  .live-help svg { position: absolute; left: 9px; top: 100px; }
</style>
</head>
<body>

<header class="abs topbar"></header>
<div class="abs brand"><span class="brand-mark"></span>BrightKestrel</div>

<div class="abs photo-strip">
  <div class="ph-arch" role="img" aria-label="Photo of a stone arch ruin on a golden hillside under a blue sky"></div>
  <div class="ph-festival" role="img" aria-label="Photo of a child in a colourful flower headdress"></div>
  <div class="ph-canal" role="img" aria-label="Photo of a boat loaded with flowers on a misty canal"></div>
  <div class="ph-study" role="img" aria-label="Black and white photo of a man seated in a study"></div>
  <div class="ph-gathering" role="img" aria-label="Photo of police officers beside people in traditional dress"></div>
</div>

<h1 class="abs intro intro-title">BrightKestrel Support Center</h1>
<p class="abs intro intro-sub">Resources to provide you wiht additional insight into the worls of Photography</p>
<div class="abs rule" style="left:137px; top:380px; width:919px;"></div>

<section class="abs feature" style="left:185px; top:424px;">
  <div class="feature-icon" style="margin-left:40px;">
    <svg width="32" height="34" viewBox="0 0 32 34"><path d="M4 2 L30 17 L4 32 Z" fill="var(--red)"/></svg>
  </div>
  <h2 class="feature-title">Video Tutorials</h2>
  <p class="feature-text">Et dolore magna aliqua enim ad minim veniam, quis nostrud lum exercitation ullamco laboris nisi ut aliquip.</p>
  <a class="feature-btn">Go to Video Tutorials</a>
</section>

<section class="abs feature" style="left:498px; top:424px;">
  <div class="feature-icon" style="margin-left:40px;">
    <svg width="36" height="42" viewBox="0 0 36 42" fill="var(--red)">
      <path d="M9 9 a9 9 0 0 1 18 0 Z"/>
      <circle cx="18" cy="7" r="2.6" fill="var(--white)"/>
      <path d="M10 11 h16 a8 8 0 0 1 -16 0 Z"/>
      <path d="M2 42 v-10 a10 10 0 0 1 10 -10 h12 a10 10 0 0 1 10 10 v10 Z"/>
      <path d="M13 23 v8 a5 5 0 0 0 10 0" fill="none" stroke="var(--white)" stroke-width="2"/>
      <circle cx="23" cy="31" r="2" fill="var(--white)"/>
    </svg>
  </div>
  <h2 class="feature-title">Lorem Ipsum</h2>
  <p class="feature-text">Et dolore magna aliqua enim ad minim veniam, quis nostrud lum exercitation ullamco laboris nisi ut aliquip.</p>
  <a class="feature-btn">Go to Lorem Ipsum</a>
</section>

<section class="abs feature" style="left:816px; top:423px;">
  <div class="feature-icon" style="margin-left:40px; font-size:62px; font-weight:700; line-height:1;">?</div>
  <h2 class="feature-title">Lorem Ipsum</h2>
  <p class="feature-text">Et dolore magna aliqua enim ad minim veniam, quis nostrud lum exercitation ullamco laboris nisi ut aliquip.</p>
  <a class="feature-btn">Go to Lorem Ipsum</a>
</section>

<div class="abs rule" style="left:137px; top:760px; width:922px;"></div>
<div class="abs notch"></div>

<h2 class="abs section-title" style="left:0; width:1184px; text-align:center; top:815px;">Latest Video Tutorials</h2>
<a class="abs view-all">View all Videos</a>

<article class="abs video" style="left:207px; top:883px; width:214px;">
  <div class="video-thumb" role="img" aria-label="Video still of a woman wheeling a barrow of young orangutans" style="background:linear-gradient(160deg,#7c8a5a,#4f5f38 50%,#a86a3a);">
    <div class="play"><svg width="24" height="28" viewBox="0 0 24 28"><path d="M3 1 L23 14 L3 27 Z" fill="rgba(255,255,255,0.85)"/></svg></div>
  </div>
  <p class="video-caption">Uploading Files Using the Drag and Drop Uploader</p>
</article>

<article class="abs video" style="left:486px; top:883px; width:214px;">
  <div class="video-thumb" role="img" aria-label="Video still of a street with a large painted poster wall" style="background:linear-gradient(120deg,#8a7e66,#6c6a5c 45%,#3f5f9a 70%,#b04438);">
    <div class="play"><svg width="24" height="28" viewBox="0 0 24 28"><path d="M3 1 L23 14 L3 27 Z" fill="rgba(255,255,255,0.85)"/></svg></div>
  </div>
  <p class="video-caption">Publishing Files</p>
</article>

<article class="abs video" style="left:762px; top:883px; width:228px;">
  <div class="video-thumb" role="img" aria-label="Video still of a stone arch ruin on a golden hillside" style="background:linear-gradient(100deg,#d0922a,#e0a844 30%,#2d5c93 55%,#a87530 85%);">
    <div class="play"><svg width="24" height="28" viewBox="0 0 24 28"><path d="M3 1 L23 14 L3 27 Z" fill="rgba(255,255,255,0.85)"/></svg></div>
  </div>
  <p class="video-caption">Creating Galleries</p>
</article>

<div class="abs rule" style="left:139px; top:1116px; width:920px;"></div>

<h2 class="abs section-title" style="left:138px; top:1148px;">Frecuent Asked Questions (F.A.Q)</h2>
<h2 class="abs section-title" style="left:812px; top:1148px;">Search</h2>
<div class="abs search-box"></div>
<div class="abs search-btn"></div>

<aside class="abs live-help">
  <span>Live Help</span>
  <svg width="15" height="15" viewBox="0 0 15 15"><circle cx="7.5" cy="7" r="6" fill="var(--white)"/><path d="M3 11 L2 14 L6 12 Z" fill="var(--white)"/></svg>
</aside>

</body>
</html>
```